K&T Fixit and Rebuild general contracting business card design

I already have a logo that I want to use and I need a card that uses that logo and color scheme on the front with the address phone numbers and email and on the back a place for technicians to write in their name and phone number when they hand it out. It will need the License number of License #KTFXTRB318QN.
It should say General Contractor under the company name. The address is
4417 NE 3rd Ave, Ste D246
Vancouver, WA 98612
www.kandtfixitandrebuild.example
office@kandtfixitandrebuild.example
360-555-0182 is the telephone number
360-555-0149 is the fax number

Target Market(s)

Homeowners needing remodel work or repairs in their home.

Industry/Entity Type

Construction

Contact Information for Business Card

Business name, address, phone number, license number, fax number, email, and website on the front and a place to fill in technician's name and number

Font styles to use
Serif

Requirements
Must have
• Business name, address, phone number, license number, fax number, email, and website on the front and a place to fill in technician's name and number
Nice to have
• I uploaded an example of a front that is good.
Should not have
• Froo froo or extra embellishments.

```html
<!DOCTYPE html>
<html lang="en">
<head>
<meta charset="utf-8">
<title>K&amp;T Fixit and Rebuild – Business Card</title>
<link rel="stylesheet" href="https://fonts.googleapis.com/css2?family=Montserrat:wght@400;500;700&display=swap">
<style>
  :root {
    --canvas: #d8d8d6;
    --card: #ececeb;
    --card-light: #f4f4f3;
    --ink: #1b1b1b;
    --panel: #1d1d1d;
    --copper: #c27a4c;
    --copper-dark: #b06a3d;
    --text: #2a2a2a;
    --muted: #6a6a6a;
  }
  * { box-sizing: border-box; margin: 0; padding: 0; }
  html, body { width: 1200px; height: 800px; overflow: hidden; }
  body {
    background: var(--canvas);
    font-family: "Montserrat", sans-serif;
    color: var(--text);
    position: relative;
  }
  .card {
    position: absolute;
    left: 364px;
    width: 472px;
    height: 262px;
    background: linear-gradient(135deg, var(--card) 0%, var(--card-light) 60%, var(--card) 100%);
    box-shadow: 0 2px 6px rgba(0,0,0,0.12);
    overflow: hidden;
  }
  .card--front { top: 125px; }
  .card--back { top: 421px; }

  .brand-panel {
    position: absolute;
    left: 29px; top: 0;
    width: 147px; height: 183px;
    background: var(--panel);
    border-radius: 0 0 5px 5px;
    display: flex; align-items: center; justify-content: center;
  }
  .brand-name {
    font-family: "Montserrat", sans-serif;
    font-weight: 700;
    color: var(--copper);
    text-align: center;
    line-height: 1.15;
  }
  .brand-panel .brand-name { font-size: 15px; }

  .license {
    position: absolute;
    left: 29px; top: 200px;
    width: 147px;
    text-align: center;
    font-size: 9px; font-weight: 500;
    color: var(--text);
    white-space: nowrap;
  }
  .license strong { color: var(--copper); font-weight: 500; }

  .company {
    position: absolute;
    left: 205px; top: 40px;
    width: 232px;
  }
  .company__name {
    font-size: 16px;
    font-weight: 700;
    color: var(--ink);
    letter-spacing: -0.2px;
    white-space: nowrap;
  }
  .company__role {
    display: flex; align-items: center; gap: 5px;
    margin-top: 2px;
    font-size: 10px; font-weight: 500;
    color: var(--copper);
  }
  .company__role::after {
    content: ""; flex: 1;
    height: 1.5px; background: var(--ink);
  }

  .address {
    position: absolute;
    left: 205px; top: 106px;
    font-style: normal;
    font-size: 11px; line-height: 14px;
    color: var(--text);
  }
  .address::after {
    content: ""; display: block;
    width: 53px; height: 1px;
    background: var(--ink);
    margin: 5px 0 0 -2px;
  }

  .contacts {
    position: absolute;
    left: 205px; top: 147px;
    list-style: none;
  }
  .contacts li {
    display: flex; align-items: center;
    height: 18px; margin-bottom: 4px;
    font-size: 11px; color: var(--text);
  }
  .contacts .icon {
    width: 18px; height: 18px;
    border-radius: 50%;
    background: var(--copper);
    margin-right: 9px;
    flex: none;
    display: flex; align-items: center; justify-content: center;
  }
  .contacts svg { width: 11px; height: 11px; }

  .band {
    position: absolute;
    top: 52px; width: 32px; height: 158px;
    background: linear-gradient(180deg, var(--copper) 0%, var(--copper-dark) 100%);
  }
  .band--left { left: 0; border-radius: 0 5px 5px 0; }
  .band--right { right: 0; border-radius: 5px 0 0 5px; }
  .card--back .brand-name {
    position: absolute;
    left: 0; right: 0; top: 72px;
    font-size: 19px;
  }
  .write-in {
    position: absolute;
    left: 82px; right: 82px; top: 124px;
  }
  .write-in__field {
    display: flex; align-items: flex-end; gap: 8px;
    height: 22px; margin-bottom: 14px;
    font-size: 10px; font-weight: 500;
    color: var(--muted);
  }
  .write-in__field::after {
    content: ""; flex: 1;
    height: 1px; background: var(--ink);
    margin-bottom: 2px;
  }
</style>
</head>
<body>
  <section class="card card--front" aria-label="Card front">
    <div class="brand-panel">
      <p class="brand-name">K&amp;T Fixit<br>and Rebuild</p>
    </div>
    <p class="license">License # <strong>KTFXTRB318QN</strong></p>
    <header class="company">
      <h1 class="company__name">K&amp;T FIXIT AND REBUILD</h1>
      <p class="company__role">General Contractor</p>
    </header>
    <address class="address">
      4417 NE 3rd Ave, Ste D246<br>
      Vancouver, WA 98612
    </address>
    <ul class="contacts">
      <li><span class="icon"><svg viewBox="0 0 12 12" fill="#fff"><path d="M1 4c0-1.5 2.2-2.5 5-2.5s5 1 5 2.5v1H8.5V4h-5v1H1z"/><rect x="2.5" y="6" width="7" height="4.5" rx="1"/></svg></span>360-555-0182</li>
      <li><span class="icon"><svg viewBox="0 0 12 12" fill="#fff"><rect x="3" y="1" width="6" height="3"/><rect x="1" y="4.5" width="10" height="4.5" rx="1"/><rect x="3" y="7.5" width="6" height="3.5" fill="#fff" stroke="#c27a4c" stroke-width=".6"/></svg></span>360-555-0149</li>
      <li><span class="icon"><svg viewBox="0 0 12 12" fill="none" stroke="#fff" stroke-width="1"><rect x="1.5" y="3" width="9" height="6"/><path d="M1.5 3L6 7l4.5-4M1.5 9l3.3-3M10.5 9L7.2 6"/></svg></span>office@kandtfixitandrebuild.example</li>
      <li><span class="icon"><svg viewBox="0 0 12 12" fill="none" stroke="#fff" stroke-width=".9"><circle cx="6" cy="6" r="4.5"/><ellipse cx="6" cy="6" rx="2" ry="4.5"/><path d="M1.5 6h9M2.3 3.5h7.4M2.3 8.5h7.4"/></svg></span>www.kandtfixitandrebuild.example</li>
    </ul>
  </section>

  <section class="card card--back" aria-label="Card back">
    <div class="band band--left"></div>
    <p class="brand-name">K&amp;T Fixit and Rebuild</p>
    <div class="write-in">
      <p class="write-in__field">Technician</p>
      <p class="write-in__field">Phone</p>
    </div>
    <div class="band band--right"></div>
  </section>
</body>
</html>
```